Brochure for Law Support Services Company

Hi
I need a 2-fold brochure for my small company. We provide office services for law firms in Brazil. The company website is this one: www.vtamplexo.com.br
A law firm can have an internal admin team that does all bureaucratic/official work at tribunals.  These services range from lawsuits copies, certification, registrar and we also perform official duties like representing law firms in judgements. It is costly for customers to do this in-house as they lack scale and expertise.
My company offer outsource this services, with the following advantages:
1) We offer countrywide coverage
2) Customers can order and follow their service online
3) We have agreed pre-defined prices
4) We guarantee timeliness and accuracy
We achieve this thru 3 pillars: expertise, process and technology.
I need a brochure that has some basic sessions, describing our services, how we work and the value we provide. You dont need to write in Portuguese, but I need the structure so I can fill the gaps with text.
For example, I need a Brazilian map showing our coverage, the 3 pillars, an area for a case study, a session that shows our value prop.
Thanks
Nelo

Target Market(s)
Law firms
Industry/Entity Type
Law Firm
Requirements
Must have
- Professional - example attached
Logo attached
If someone make me one like the one I attached it will have higher chance to win (instead of Australia map) I need a brazilian on the same look/feel
Should not have
- Casual look

```html
<!DOCTYPE html>
<html lang="en">
<head>
<meta charset="utf-8">
<title>Vtamplexo – Brochure Colour Options</title>
<link rel="stylesheet" href="https://fonts.googleapis.com/css2?family=Open+Sans:wght@300;400;600;700&family=Roboto+Condensed:wght@400&display=swap">
<style>
:root{
  --stage:#3a3a3a;
  --board:#2f2f2f;
  --plum:#8c1d55;
  --grey:#8a8a8a;
  --grey-dark:#6f6f6f;
  --black:#111;
  --paper:#fff;
  --ink:#4a4a4a;
  --option-num:#d0d0d0;
  --photo-warm:linear-gradient(135deg,#6b5a4e 0%,#b9a592 45%,#e6d9c6 70%,#8a7563 100%);
  --photo-cool:linear-gradient(135deg,#4e6f8e 0%,#a7bccf 55%,#e6edf3 100%);
  --coverage:linear-gradient(160deg,#c98aa9 0%,#a8396e 55%,#8c1d55 100%);
}
*{box-sizing:border-box;margin:0;padding:0}
html,body{width:1200px;height:1000px;overflow:hidden;background:var(--stage);font-family:"Open Sans",Arial,sans-serif}
.board{position:relative;width:1200px;height:1000px}
.option{position:absolute;width:584px;height:484px;background:var(--board)}
.option--1{left:8px;top:8px;--services:var(--grey);--caption:var(--plum);--bar:var(--plum);--edge:var(--plum)}
.option--2{left:608px;top:8px;--services:var(--plum);--caption:var(--plum);--bar:var(--grey-dark);--edge:var(--plum)}
.option--3{left:8px;top:508px;--services:var(--plum);--caption:var(--plum);--bar:var(--grey);--edge:var(--plum)}
.option--4{left:608px;top:508px;--services:var(--grey);--caption:var(--grey);--bar:var(--plum);--edge:var(--plum)}
.option__number{position:absolute;left:70px;top:78px;font-size:92px;font-weight:600;color:var(--option-num);line-height:1}

.sheet{position:absolute;background:var(--paper)}
.outside{left:214px;top:22px;width:350px;height:245px;z-index:2}
.inside{left:14px;top:222px;width:340px;height:235px;z-index:1}
.block{position:absolute}
.outside .strip-left{left:0;top:15px;width:12px;height:120px;background:var(--edge)}
.outside .strip-left-low{left:0;top:135px;width:12px;height:35px;background:var(--black)}
.services{left:12px;top:15px;width:148px;height:155px;background:var(--services);color:#fff;padding:4px 7px}
.heading{font-size:9px;font-weight:400;padding-bottom:2px;border-bottom:1px solid currentColor;position:relative;width:62%;white-space:nowrap}
.heading__lead{color:var(--plum)}
.services .heading__lead{color:#fff;opacity:.85}
.option--1 .services .heading__lead,.option--4 .services .heading__lead{color:var(--plum);opacity:1}
.heading::after{content:"";position:absolute;left:24px;bottom:-5px;border:4px solid transparent;border-top-color:var(--black);border-bottom:0}
.services__cols{display:grid;grid-template-columns:1fr 1fr;gap:6px 6px;margin-top:9px}
.service{font-size:4.6px;line-height:1.45;font-weight:600}
.outside .mid-strip{left:163px;top:15px;width:22px;height:120px;background:var(--black)}
.outside .mid-strip-low{left:163px;top:135px;width:22px;height:35px;background:var(--edge)}
.cover-photo{left:193px;top:15px;width:137px;height:120px;background:var(--photo-warm)}
.outside .strip-right{left:333px;top:15px;width:17px;height:120px;background:var(--edge)}
.outside .strip-right-low{left:333px;top:135px;width:17px;height:35px;background:var(--black)}
.caption{left:193px;top:135px;width:137px;height:35px;background:var(--caption);color:#fff;font-family:"Roboto Condensed","Arial Narrow",sans-serif;font-size:8px;line-height:1.35;text-align:right;padding:7px 5px 0 4px;white-space:nowrap}
.intro-bar{left:12px;top:180px;width:148px;height:23px;background:var(--bar);color:#fff;font-size:4.4px;font-weight:600;line-height:1.35;text-align:center;padding:3px 5px}
.brand{left:232px;top:196px;display:flex;align-items:center;gap:5px}
.brand__mark{width:14px;height:14px;background:var(--plum)}
.brand__name{font-size:11px;font-weight:400;color:var(--ink);letter-spacing:.5px;line-height:1}
.brand__tag{font-size:4.6px;color:var(--ink);margin-top:2px}

.inside .strip-left{left:0;top:15px;width:10px;height:105px;background:var(--plum)}
.inside .strip-right{left:328px;top:15px;width:12px;height:105px;background:var(--grey)}
.value{left:18px;top:10px;width:150px;color:var(--ink)}
.value__body{display:grid;grid-template-columns:102px 44px;gap:4px;margin-top:8px;font-size:4.4px;line-height:1.4}
.value__body p{margin-bottom:4px}
.value__body p.accent{color:var(--plum)}
.work{left:178px;top:10px;width:140px;color:var(--ink)}
.coverage-map{left:218px;top:40px;width:62px;height:84px;background:var(--coverage);border-radius:2px}
.map-note{position:absolute;display:flex;align-items:center;gap:2px;font-size:3.6px;color:var(--plum);white-space:nowrap}
.map-note::after{content:"";display:block;width:18px;height:.6px;background:var(--grey)}
.map-note--right{flex-direction:row-reverse}
.tiles{top:128px;display:flex;gap:2px}
.tiles--value{left:14px}
.tiles--work{left:178px}
.inside .base-black{left:0;top:128px;width:12px;height:105px;background:var(--black)}
.tile{width:47px;display:flex;flex-direction:column;gap:2px}
.tile__photo{height:40px;position:relative}
.tile__photo--warm{background:var(--photo-warm)}
.tile__photo--cool{background:var(--photo-cool)}
.tile__label{position:absolute;left:0;top:0;background:rgba(0,0,0,.45);color:#fff;font-size:6px;padding:1px 3px}
.tile__text{height:62px;padding:3px;font-size:3.9px;line-height:1.4;color:#fff}
.tile__text--plum{background:var(--plum)}
.tile__text--grey{background:var(--grey)}
.tile__text--dark{background:var(--grey-dark)}
</style>
</head>
<body>
<main class="board">

  <section class="option option--1">
    <div class="option__number">1</div>
    <div class="sheet outside">
      <div class="block strip-left"></div><div class="block strip-left-low"></div>
      <div class="block services">
        <h2 class="heading"><span class="heading__lead">Our</span> Services</h2>
        <div class="services__cols">
          <p class="service">• Lawsuit copies obtained at any court and delivered on the agreed date.</p>
          <p class="service">• Certifications and registrar filings handled from request to return.</p>
          <p class="service">• Hearings attended on behalf of your firm by trained staff.</p>
          <p class="service">• Petition filing at state and federal courts across the country.</p>
        </div>
      </div>
      <div class="block mid-strip"></div><div class="block mid-strip-low"></div>
      <div class="block cover-photo" role="img" aria-label="Photo of a fountain pen resting on a handwritten legal document"></div>
      <div class="block strip-right"></div><div class="block strip-right-low"></div>
      <div class="block caption">Difficulty on insensible<br>reasonable in. From as went he they</div>
      <div class="block intro-bar">Started earned brother believe an exposed so. Me he believing daughters if forfeited at furniture. Age again and stuff downs spoke. Late hour new nay able fat each sell.</div>
      <div class="block brand"><span class="brand__mark"></span><div><div class="brand__name">VTAMPLEXO</div><div class="brand__tag">Serviços de Apoio Jurídico</div></div></div>
    </div>
    <div class="sheet inside">
      <div class="block strip-left"></div><div class="block strip-right"></div>
      <div class="block value">
        <h2 class="heading"><span class="heading__lead">Our</span> Value</h2>
        <div class="value__body">
          <div>
            <p>Countrywide coverage through a network of partners present at every major court in Brazil.</p>
            <p class="accent">Order and follow each service online, with status updates at every step.</p>
            <p>Agreed prices defined upfront, so your firm always knows the cost.</p>
          </div>
          <div><p>"Timely and accurate, every single time."</p><p>Guaranteed deadlines and checked results.</p></div>
        </div>
      </div>
      <div class="block work"><h2 class="heading"><span class="heading__lead">Our</span> Work</h2></div>
      <div class="block coverage-map" role="img" aria-label="Map of Brazil showing national coverage"></div>
      <span class="map-note" style="left:178px;top:66px">North region</span>
      <span class="map-note" style="left:182px;top:100px">Central west</span>
      <span class="map-note map-note--right" style="left:262px;top:114px">Southeast</span>
      <div class="block base-black"></div>
      <div class="block tiles tiles--value">
        <div class="tile"><div class="tile__photo tile__photo--warm" role="img" aria-label="Photo of court files"></div><p class="tile__text tile__text--plum">Case study: a firm cut admin costs by outsourcing its court errands.</p></div>
        <div class="tile"><div class="tile__photo tile__photo--cool" role="img" aria-label="Photo of a lawyer at work"></div><p class="tile__text tile__text--grey">Copies delivered in two days across four states.</p></div>
        <div class="tile"><div class="tile__photo tile__photo--cool" role="img" aria-label="Photo of a globe"></div><p class="tile__text tile__text--plum">Nationwide reach without local staff or offices.</p></div>
      </div>
      <div class="block tiles tiles--work">
        <div class="tile"><div class="tile__photo tile__photo--cool" role="img" aria-label="Photo representing process"><span class="tile__label">Process</span></div><p class="tile__text tile__text--dark">Standard steps for every order, checked twice.</p></div>
        <div class="tile"><div class="tile__photo tile__photo--warm" role="img" aria-label="Photo of law books"><span class="tile__label">Expertise</span></div><p class="tile__text tile__text--plum">Years of practice at courts and registrars.</p></div>
        <div class="tile"><div class="tile__photo tile__photo--cool" role="img" aria-label="Photo representing technology"><span class="tile__label">Technology</span></div><p class="tile__text tile__text--grey">Online ordering and live tracking portal.</p></div>
      </div>
    </div>
  </section>

  <section class="option option--2">
    <div class="option__number">2</div>
    <div class="sheet outside">
      <div class="block strip-left"></div><div class="block strip-left-low"></div>
      <div class="block services">
        <h2 class="heading"><span class="heading__lead">Our</span> Services</h2>
        <div class="services__cols">
          <p class="service">• Lawsuit copies obtained at any court and delivered on the agreed date.</p>
          <p class="service">• Certifications and registrar filings handled from request to return.</p>
          <p class="service">• Hearings attended on behalf of your firm by trained staff.</p>
          <p class="service">• Petition filing at state and federal courts across the country.</p>
        </div>
      </div>
      <div class="block mid-strip"></div><div class="block mid-strip-low"></div>
      <div class="block cover-photo" role="img" aria-label="Photo of a fountain pen resting on a handwritten legal document"></div>
      <div class="block strip-right"></div><div class="block strip-right-low"></div>
      <div class="block caption">Difficulty on insensible<br>reasonable in. From as went he they</div>
      <div class="block intro-bar">Started earned brother believe an exposed so. Me he believing daughters if forfeited at furniture. Age again and stuff downs spoke. Late hour new nay able fat each sell.</div>
      <div class="block brand"><span class="brand__mark"></span><div><div class="brand__name">VTAMPLEXO</div><div class="brand__tag">Serviços de Apoio Jurídico</div></div></div>
    </div>
    <div class="sheet inside">
      <div class="block strip-left"></div><div class="block strip-right"></div>
      <div class="block value">
        <h2 class="heading"><span class="heading__lead">Our</span> Value</h2>
        <div class="value__body">
          <div>
            <p>Countrywide coverage through a network of partners present at every major court in Brazil.</p>
            <p class="accent">Order and follow each service online, with status updates at every step.</p>
            <p>Agreed prices defined upfront, so your firm always knows the cost.</p>
          </div>
          <div><p>"Timely and accurate, every single time."</p><p>Guaranteed deadlines and checked results.</p></div>
        </div>
      </div>
      <div class="block work"><h2 class="heading"><span class="heading__lead">Our</span> Work</h2></div>
      <div class="block coverage-map" role="img" aria-label="Map of Brazil showing national coverage"></div>
      <span class="map-note" style="left:178px;top:66px">North region</span>
      <span class="map-note" style="left:182px;top:100px">Central west</span>
      <span class="map-note map-note--right" style="left:262px;top:114px">Southeast</span>
      <div class="block base-black"></div>
      <div class="block tiles tiles--value">
        <div class="tile"><div class="tile__photo tile__photo--warm" role="img" aria-label="Photo of court files"></div><p class="tile__text tile__text--plum">Case study: a firm cut admin costs by outsourcing its court errands.</p></div>
        <div class="tile"><div class="tile__photo tile__photo--cool" role="img" aria-label="Photo of a lawyer at work"></div><p class="tile__text tile__text--grey">Copies delivered in two days across four states.</p></div>
        <div class="tile"><div class="tile__photo tile__photo--cool" role="img" aria-label="Photo of a globe"></div><p class="tile__text tile__text--dark">Nationwide reach without local staff or offices.</p></div>
      </div>
      <div class="block tiles tiles--work">
        <div class="tile"><div class="tile__photo tile__photo--cool" role="img" aria-label="Photo representing process"><span class="tile__label">Process</span></div><p class="tile__text tile__text--dark">Standard steps for every order, checked twice.</p></div>
        <div class="tile"><div class="tile__photo tile__photo--warm" role="img" aria-label="Photo of law books"><span class="tile__label">Expertise</span></div><p class="tile__text tile__text--plum">Years of practice at courts and registrars.</p></div>
        <div class="tile"><div class="tile__photo tile__photo--cool" role="img" aria-label="Photo representing technology"><span class="tile__label">Technology</span></div><p class="tile__text tile__text--grey">Online ordering and live tracking portal.</p></div>
      </div>
    </div>
  </section>

  <section class="option option--3">
    <div class="option__number">3</div>
    <div class="sheet outside">
      <div class="block strip-left"></div><div class="block strip-left-low"></div>
      <div class="block services">
        <h2 class="heading"><span class="heading__lead">Our</span> Services</h2>
        <div class="services__cols">
          <p class="service">• Lawsuit copies obtained at any court and delivered on the agreed date.</p>
          <p class="service">• Certifications and registrar filings handled from request to return.</p>
          <p class="service">• Hearings attended on behalf of your firm by trained staff.</p>
          <p class="service">• Petition filing at state and federal courts across the country.</p>
        </div>
      </div>
      <div class="block mid-strip"></div><div class="block mid-strip-low"></div>
      <div class="block cover-photo" role="img" aria-label="Photo of a fountain pen resting on a handwritten legal document"></div>
      <div class="block strip-right"></div><div class="block strip-right-low"></div>
      <div class="block caption">Difficulty on insensible<br>reasonable in. From as went he they</div>
      <div class="block intro-bar">Started earned brother believe an exposed so. Me he believing daughters if forfeited at furniture. Age again and stuff downs spoke. Late hour new nay able fat each sell.</div>
      <div class="block brand"><span class="brand__mark"></span><div><div class="brand__name">VTAMPLEXO</div><div class="brand__tag">Serviços de Apoio Jurídico</div></div></div>
    </div>
    <div class="sheet inside">
      <div class="block strip-left"></div><div class="block strip-right"></div>
      <div class="block value">
        <h2 class="heading"><span class="heading__lead">Our</span> Value</h2>
        <div class="value__body">
          <div>
            <p>Countrywide coverage through a network of partners present at every major court in Brazil.</p>
            <p class="accent">Order and follow each service online, with status updates at every step.</p>
            <p>Agreed prices defined upfront, so your firm always knows the cost.</p>
          </div>
          <div><p>"Timely and accurate, every single time."</p><p>Guaranteed deadlines and checked results.</p></div>
        </div>
      </div>
      <div class="block work"><h2 class="heading"><span class="heading__lead">Our</span> Work</h2></div>
      <div class="block coverage-map" role="img" aria-label="Map of Brazil showing national coverage"></div>
      <span class="map-note" style="left:178px;top:66px">North region</span>
      <span class="map-note" style="left:182px;top:100px">Central west</span>
      <span class="map-note map-note--right" style="left:262px;top:114px">Southeast</span>
      <div class="block base-black"></div>
      <div class="block tiles tiles--value">
        <div class="tile"><div class="tile__photo tile__photo--warm" role="img" aria-label="Photo of court files"></div><p class="tile__text tile__text--grey">Case study: a firm cut admin costs by outsourcing its court errands.</p></div>
        <div class="tile"><div class="tile__photo tile__photo--cool" role="img" aria-label="Photo of a lawyer at work"></div><p class="tile__text tile__text--plum">Copies delivered in two days across four states.</p></div>
        <div class="tile"><div class="tile__photo tile__photo--cool" role="img" aria-label="Photo of a globe"></div><p class="tile__text tile__text--grey">Nationwide reach without local staff or offices.</p></div>
      </div>
      <div class="block tiles tiles--work">
        <div class="tile"><div class="tile__photo tile__photo--cool" role="img" aria-label="Photo representing process"><span class="tile__label">Process</span></div><p class="tile__text tile__text--grey">Standard steps for every order, checked twice.</p></div>
        <div class="tile"><div class="tile__photo tile__photo--warm" role="img" aria-label="Photo of law books"><span class="tile__label">Expertise</span></div><p class="tile__text tile__text--plum">Years of practice at courts and registrars.</p></div>
        <div class="tile"><div class="tile__photo tile__photo--cool" role="img" aria-label="Photo representing technology"><span class="tile__label">Technology</span></div><p class="tile__text tile__text--grey">Online ordering and live tracking portal.</p></div>
      </div>
    </div>
  </section>

  <section class="option option--4">
    <div class="option__number">4</div>
    <div class="sheet outside">
      <div class="block strip-left"></div><div class="block strip-left-low"></div>
      <div class="block services">
        <h2 class="heading"><span class="heading__lead">Our</span> Services</h2>
        <div class="services__cols">
          <p class="service">• Lawsuit copies obtained at any court and delivered on the agreed date.</p>
          <p class="service">• Certifications and registrar filings handled from request to return.</p>
          <p class="service">• Hearings attended on behalf of your firm by trained staff.</p>
          <p class="service">• Petition filing at state and federal courts across the country.</p>
        </div>
      </div>
      <div class="block mid-strip"></div><div class="block mid-strip-low"></div>
      <div class="block cover-photo" role="img" aria-label="Photo of a fountain pen resting on a handwritten legal document"></div>
      <div class="block strip-right"></div><div class="block strip-right-low"></div>
      <div class="block caption">Difficulty on insensible<br>reasonable in. From as went he they</div>
      <div class="block intro-bar">Started earned brother believe an exposed so. Me he believing daughters if forfeited at furniture. Age again and stuff downs spoke. Late hour new nay able fat each sell.</div>
      <div class="block brand"><span class="brand__mark"></span><div><div class="brand__name">VTAMPLEXO</div><div class="brand__tag">Serviços de Apoio Jurídico</div></div></div>
    </div>
    <div class="sheet inside">
      <div class="block strip-left"></div><div class="block strip-right"></div>
      <div class="block value">
        <h2 class="heading"><span class="heading__lead">Our</span> Value</h2>
        <div class="value__body">
          <div>
            <p>Countrywide coverage through a network of partners present at every major court in Brazil.</p>
            <p class="accent">Order and follow each service online, with status updates at every step.</p>
            <p>Agreed prices defined upfront, so your firm always knows the cost.</p>
          </div>
          <div><p>"Timely and accurate, every single time."</p><p>Guaranteed deadlines and checked results.</p></div>
        </div>
      </div>
      <div class="block work"><h2 class="heading"><span class="heading__lead">Our</span> Work</h2></div>
      <div class="block coverage-map" role="img" aria-label="Map of Brazil showing national coverage"></div>
      <span class="map-note" style="left:178px;top:66px">North region</span>
      <span class="map-note" style="left:182px;top:100px">Central west</span>
      <span class="map-note map-note--right" style="left:262px;top:114px">Southeast</span>
      <div class="block base-black"></div>
      <div class="block tiles tiles--value">
        <div class="tile"><div class="tile__photo tile__photo--warm" role="img" aria-label="Photo of court files"></div><p class="tile__text tile__text--plum">Case study: a firm cut admin costs by outsourcing its court errands.</p></div>
        <div class="tile"><div class="tile__photo tile__photo--cool" role="img" aria-label="Photo of a lawyer at work"></div><p class="tile__text tile__text--grey">Copies delivered in two days across four states.</p></div>
        <div class="tile"><div class="tile__photo tile__photo--cool" role="img" aria-label="Photo of a globe"></div><p class="tile__text tile__text--plum">Nationwide reach without local staff or offices.</p></div>
      </div>
      <div class="block tiles tiles--work">
        <div class="tile"><div class="tile__photo tile__photo--cool" role="img" aria-label="Photo representing process"><span class="tile__label">Process</span></div><p class="tile__text tile__text--plum">Standard steps for every order, checked twice.</p></div>
        <div class="tile"><div class="tile__photo tile__photo--warm" role="img" aria-label="Photo of law books"><span class="tile__label">Expertise</span></div><p class="tile__text tile__text--grey">Years of practice at courts and registrars.</p></div>
        <div class="tile"><div class="tile__photo tile__photo--cool" role="img" aria-label="Photo representing technology"><span class="tile__label">Technology</span></div><p class="tile__text tile__text--plum">Online ordering and live tracking portal.</p></div>
      </div>
    </div>
  </section>

</main>
</body>
</html>
```